Business Stationery Design

I would like to get some stationery designed for my company. The stationery should include a letterhead, envelope, and business card. We are a technology consulting company specializing in Healthcare IT, and Education management systems. The colors of the stationery should match the logo. The logo is uploaded.

Target Market(s)

Hospitals, Clinics. Doctors offices. Private Schools.

Industry/Entity Type

Business

```html
<!DOCTYPE html>
<html lang="en">
<head>
<meta charset="UTF-8">
<title>Clearbrook Consulting Group – Business Card</title>
<link rel="stylesheet" href="https://fonts.googleapis.com/css2?family=Open+Sans:wght@400;600&family=Arimo:wght@400;700&display=swap">
<style>
  :root {
    --stage: #1d1d1d;
    --paper: #f1f1f1;
    --leaf: #6cbf46;
    --leaf-light: #86cc5e;
    --sun: #f0b81d;
    --ink-light: #ffffff;
  }
  * { margin: 0; padding: 0; box-sizing: border-box; }
  html, body {
    width: 1200px; height: 900px; overflow: hidden;
    background: var(--stage);
  }
  .stage {
    width: 1200px; height: 900px;
    display: flex; flex-direction: column;
    align-items: center; justify-content: center; gap: 48px;
  }
  .card {
    width: 640px; height: 366px;
    border-radius: 18px; overflow: hidden;
    position: relative;
  }
  /* Front */
  .card-front { display: flex; background: var(--paper); }
  .brand-panel {
    width: 300px; height: 100%;
    display: flex; align-items: center; justify-content: center;
    position: relative;
  }
  .brand-panel::after {
    content: ""; position: absolute; right: 10px; top: 0;
    width: 4px; height: 100%; background: var(--sun);
  }
  .brand-name {
    display: flex; align-items: center; gap: 10px;
    font-family: "Open Sans", sans-serif; font-weight: 600;
    font-size: 24px; line-height: 1.15; color: var(--leaf);
  }
  .brand-dot {
    width: 18px; height: 18px; border-radius: 50%;
    background: var(--leaf); flex: none;
  }
  .details-panel {
    flex: 1;
    background: linear-gradient(135deg, var(--leaf) 0%, var(--leaf-light) 60%, var(--leaf) 100%);
    color: var(--ink-light);
    padding: 70px 0 0 44px;
    font-family: "Arimo", sans-serif;
  }
  .person-name { font-weight: 700; font-size: 28px; }
  .person-role { font-size: 19px; margin-top: 2px; }
  .address { font-size: 15px; line-height: 1.45; margin-top: 22px; }
  .contact-list { list-style: none; margin-top: 18px; font-size: 15px; line-height: 1.6; }
  .contact-list li { display: flex; align-items: center; gap: 9px; }
  .contact-list svg { width: 13px; height: 13px; flex: none; }
  /* Back */
  .card-back {
    background: linear-gradient(135deg, var(--leaf) 0%, var(--leaf-light) 55%, var(--leaf) 100%);
    display: flex; flex-direction: column; align-items: center; justify-content: center; gap: 34px;
  }
  .card-back .brand-name { color: var(--ink-light); font-size: 30px; }
  .card-back .brand-dot { background: var(--ink-light); width: 22px; height: 22px; }
  .back-web {
    font-family: "Arimo", sans-serif; font-size: 15px;
    color: var(--ink-light); opacity: 0.9;
  }
</style>
</head>
<body>
<main class="stage">
  <section class="card card-front">
    <div class="brand-panel">
      <div class="brand-name"><span class="brand-dot"></span><span>Clearbrook<br>Consulting Group</span></div>
    </div>
    <div class="details-panel">
      <p class="person-name">Daniel Hart</p>
      <p class="person-role">President</p>
      <p class="address">Level 5, 120 Harbour Road<br>Northport, VIC 3100</p>
      <ul class="contact-list">
        <li><svg viewBox="0 0 16 16" fill="#fff"><path d="M3 1l3 3-2 2c1 2 3 4 5 5l2-2 3 3-2 2C7 14 2 9 1 3z"/></svg>555 014 2290</li>
        <li><svg viewBox="0 0 16 16" fill="none" stroke="#fff" stroke-width="1.6"><rect x="4" y="1" width="8" height="14" rx="1.5"/><line x1="7" y1="12.5" x2="9" y2="12.5"/></svg>555 018 3342</li>
        <li><svg viewBox="0 0 16 16" fill="#fff"><path d="M1 3h14v10H1z"/><path d="M1 3l7 6 7-6" fill="none" stroke="#6cbf46" stroke-width="1.4"/></svg>info@clearbrookgroup.com</li>
        <li><svg viewBox="0 0 16 16" fill="none" stroke="#fff" stroke-width="1.4"><circle cx="8" cy="8" r="6.5"/><ellipse cx="8" cy="8" rx="3" ry="6.5"/><line x1="1.5" y1="8" x2="14.5" y2="8"/></svg>www.clearbrookgroup.com</li>
      </ul>
    </div>
  </section>
  <section class="card card-back">
    <div class="brand-name"><span class="brand-dot"></span><span>Clearbrook Consulting Group</span></div>
    <p class="back-web">www.clearbrookgroup.com</p>
  </section>
</main>
</body>
</html>
```